タイトル 「週末ガーデナーのための水やり流・花咲かせ節約術」
サブタイトル 「毎日が楽になる5つの習慣」

上記の表紙デザインをお願いします。基本お任せします。
本の内容  原稿を添付します。

その他ご不明な点がございましたらお気楽にご質問ください。よろしくお願いいたします。
著者名 星空ナビゲーター 森川佳代 from神戸

本の内容とよくマッチしたデザインだと思いました。インパクトもあり本の対象であるアラフォーの好みと合っているように思いました。

沢山のご応募ありがとうございました。何もかもか初めての作業で、不安でしたが、関心を持っていただいて心からありがたく思っております。これからも電子書籍の出版を考えております。ご縁がありましたらまた、今後もよろしくお願いします。
ありがとうございました。

```html
<!DOCTYPE html>
<html lang="ja">
<head>
<meta charset="utf-8">
<title>週末ガーデナーのための水やり流・花咲かせ節約術</title>
<link rel="stylesheet" href="https://fonts.googleapis.com/css2?family=M+PLUS+Rounded+1c:wght@800&family=Noto+Sans+JP:wght@700;900&family=Shippori+Mincho:wght@600;800&family=Great+Vibes&family=Playfair+Display:ital,wght@1,700&display=swap">
<style>
  :root {
    --yellow: #f6d72e;
    --yellow-light: #fcef8e;
    --panel: #ffffff;
    --gold: #c9a64a;
    --red: #d8232e;
    --red-soft: #d9384a;
    --ink: #1d1d1d;
    --gold-num: #c99a2e;
  }
  * { margin: 0; padding: 0; box-sizing: border-box; }
  html, body { width: 751px; height: 1200px; overflow: hidden; }
  body { background: #ffffff; }
  .cover {
    position: relative;
    width: 751px; height: 1200px; overflow: hidden;
    background: radial-gradient(ellipse at 50% 40%, var(--yellow-light) 0%, var(--yellow) 70%);
  }
  .title-panel {
    position: absolute; left: 45px; top: 18px; width: 660px; height: 712px;
    background: var(--panel);
    border-radius: 28px;
    box-shadow: 0 0 0 3px var(--panel), 0 0 0 5px var(--gold);
  }
  .title-panel::after {
    content: ""; position: absolute; inset: 10px;
    border: 2px solid var(--gold); border-radius: 20px;
  }
  .figure-art {
    position: absolute; left: 352px; top: 14px; width: 56px; height: 160px;
    background: linear-gradient(180deg, #f3d9c4 0%, #e58bb0 55%, #f2c7d6 100%);
    border-radius: 28px 28px 8px 8px; opacity: .85;
  }
  .audience-arc { position: absolute; left: 45px; top: 30px; }
  .audience-arc text {
    font-family: "Shippori Mincho", serif; font-weight: 600;
    font-size: 32px; fill: #444;
  }
  .title { position: absolute; left: 45px; width: 660px; text-align: center;
    font-family: "M PLUS Rounded 1c", sans-serif; font-weight: 800; color: var(--red); }
  .title--style { top: 225px; font-size: 62px; color: var(--red-soft); letter-spacing: 2px; }
  .title--main { top: 310px; font-size: 112px; line-height: 1.15; letter-spacing: 4px; }
  .flower-art {
    position: absolute; left: 520px; top: 700px; width: 200px; height: 190px;
    background: radial-gradient(circle at 50% 45%, #ffffff 0%, #f4f1e4 55%, rgba(220,226,190,.6) 80%, transparent 100%);
    border-radius: 50%;
  }
  .author { position: absolute; left: 245px; top: 628px; }
  .author-role { font-family: "Noto Sans JP", sans-serif; font-weight: 900; font-size: 24px; color: var(--red); }
  .author-name { font-family: "Shippori Mincho", serif; font-weight: 800; font-size: 44px; color: var(--ink); letter-spacing: 4px; line-height: 1.2; }
  .author-from { font-family: "Great Vibes", cursive; font-size: 28px; color: var(--ink); margin-left: 6px; letter-spacing: 0; }
  .author-from span { font-family: "Shippori Mincho", serif; font-size: 22px; }
  .hands-photo {
    position: absolute; left: 0; top: 750px; width: 751px; height: 260px;
    background: linear-gradient(90deg, #cfc8c0 0%, #ecd3bd 35%, #f3dcc6 60%, #e7ddc9 100%);
    -webkit-mask-image: linear-gradient(180deg, transparent 0%, #000 20%, #000 75%, transparent 100%);
            mask-image: linear-gradient(180deg, transparent 0%, #000 20%, #000 75%, transparent 100%);
  }
  .subtitle { position: absolute; left: 0; width: 751px; text-align: center;
    font-family: "Noto Sans JP", sans-serif; font-weight: 900; color: var(--ink); }
  .subtitle--lead { top: 1018px; font-size: 48px; line-height: 1.2; letter-spacing: 14px; padding-left: 14px; }
  .subtitle--main { top: 1082px; height: 112px; font-size: 64px; letter-spacing: 6px; line-height: 112px; }
  .subtitle-number { font-family: "Playfair Display", serif; font-style: italic; font-weight: 700;
    font-size: 120px; line-height: 1; color: var(--gold-num); margin-right: 4px; }
</style>
</head>
<body>
<div class="cover">
  <div class="title-panel"></div>
  <div class="figure-art" role="img" aria-label="腕を組んで立つ女性のイラスト"></div>
  <svg class="audience-arc" width="660" height="140" viewBox="0 0 660 140">
    <path id="arc" d="M90 120 Q330 0 570 120" fill="none"/>
    <text><textPath href="#arc" startOffset="50%" text-anchor="middle">週末ガーデナーのための</textPath></text>
  </svg>
  <div class="title title--style">水やり流</div>
  <div class="title title--main">花咲かせ<br>節約術</div>
  <div class="hands-photo" role="img" aria-label="手を取り合う二人の手元の写真"></div>
  <div class="flower-art" role="img" aria-label="白い花のイラスト"></div>
  <div class="author">
    <div class="author-role">星空ナビゲーター</div>
    <div class="author-name">森川 佳代<span class="author-from">from <span>神戸</span></span></div>
  </div>
  <div class="subtitle subtitle--lead">毎日が楽になる</div>
  <div class="subtitle subtitle--main"><span class="subtitle-number">5</span>つの習慣</div>
</div>
</body>
</html>
```